We're Hiring Poster or Flyer design

We’re Hiring Details:

Positions include:
Office Manager
Office Assistant
Data Entry Techs
Outreach Manager
Asst. Outreach Manager
Events Coordinator
Drivers (must have personal car, insurance & Driver’s License)
Outreach Specialist—Walkers
Outreach Specialist—Phone/Telemarketing (evenings only)

Excellent Pay ! Fun Atmosphere ! Bonus Pay with Promotional & Career Advancement Opportunities

***************
need 3 formats of SAME flyer:
1) 8.5 x 11
2) 8.5 x 14
3) 11 x17

creative and eye catching a must; this flyer will be used on college bulletin boards and used to attract a younger demographic . . hip and chic look with "Americana style or political motif" preferred.

Target Market(s)

younger demographic . . flyer will be used during college recruiting fairs and in younger settings---age BRACKET is 21 - 35 Years old

Industry/Entity Type

Employment Agency

Font styles to use
Sans Serif

Colors

Designer to choose colors to be used in the design.

Requirements
Must have
• clean and attractive; hip; chic; simple and with good stock pics and layout
Nice to have
• american flag and patriotism
Should not have
• too much details on the job -- I only included the job announcement so you can get an idea of WHAT and WHO I am looking for . . don't list all the BORING details on the flyer/poster

```html
<!DOCTYPE html>
<html lang="en">
<head>
<meta charset="utf-8">
<title>We're Hiring – Flyer</title>
<link rel="stylesheet" href="https://fonts.googleapis.com/css2?family=Arimo:wght@400;700&family=Exo+2:wght@700;900&family=Oswald:wght@500;600;700&display=swap">
<style>
  :root{
    --backdrop:#6b6b6b;
    --paper:#f1f1f2;
    --orange:#f07a22;
    --navy:#0b3a78;
    --charcoal:#3a3a3c;
    --dark:#2f2f31;
    --teal-light:#7fb3bd;
    --teal:#1f7891;
    --coral:#d6706a;
    --mustard:#dcb424;
    --mint:#6cc3a8;
    --white:#ffffff;
  }
  *{box-sizing:border-box;margin:0;padding:0}
  html,body{width:1200px;height:1200px;overflow:hidden}
  body{background:var(--backdrop);position:relative}

  .flyer{position:absolute;left:176px;top:0;width:848px;height:1200px;background:var(--paper);overflow:hidden}

  .headline-top{position:absolute;left:38px;top:24px;font-family:"Oswald",sans-serif;font-weight:700;font-size:100px;line-height:1;color:var(--orange);letter-spacing:2px;white-space:nowrap}
  .headline-main{position:absolute;left:34px;top:118px;font-family:"Exo 2",sans-serif;font-weight:900;font-size:150px;line-height:1;color:var(--navy);letter-spacing:-3px;white-space:nowrap}

  .candidate{position:absolute;left:600px;top:88px;width:220px;text-align:center;font-family:"Oswald",sans-serif;font-weight:600;color:var(--navy);line-height:1}
  .candidate .mark{display:block;width:18px;height:18px;background:var(--navy);margin:0 auto 10px}
  .candidate .name{display:block;font-size:44px}
  .candidate .office{display:block;font-size:34px;letter-spacing:6px;margin-top:6px}

  .rule{position:absolute;left:0;width:848px;height:14px;background:var(--orange)}
  .rule.top{top:277px}
  .rule.bottom{top:743px}

  .photo{position:absolute;left:0;top:291px;width:848px;height:452px;background:linear-gradient(180deg,#e6e7ea 0%,#dadce0 70%,#c9cacd 100%)}
  .photo-people{position:absolute;left:28px;top:380px;width:800px;height:363px;border-radius:6px 6px 0 0;background:linear-gradient(90deg,#b9b5b2,#8f939c 50%,#b7b1ad)}

  .section-title{position:absolute;left:32px;top:312px;font-family:"Exo 2",sans-serif;font-weight:700;font-size:42px;line-height:1;color:var(--charcoal);letter-spacing:1px;white-space:nowrap}

  .sign{position:absolute;font-family:"Oswald",sans-serif;font-weight:500;color:var(--white);line-height:1.05;text-transform:uppercase;white-space:nowrap}
  .sign.office-manager{left:14px;top:443px;width:162px;height:111px;background:var(--teal-light);border-radius:16px;padding:16px 18px;font-size:33px}
  .sign.office-assistant{left:240px;top:378px;width:110px;height:76px;background:var(--coral);border-radius:10px;padding:12px 8px;font-size:21px;transform:rotate(12deg)}
  .sign.data-entry{left:349px;top:452px;width:148px;height:93px;background:var(--mustard);padding:18px 12px;font-size:26px}
  .sign.outreach-manager{left:540px;top:471px;width:153px;height:97px;background:var(--mint);border-radius:50%;padding:18px 6px;font-size:27px;text-align:center}
  .sign.asst-outreach{left:656px;top:311px;width:108px;height:77px;background:var(--teal);border-radius:10px;padding:10px 14px;font-size:18px;line-height:1.1}

  .roles{position:absolute;left:0;top:771px;width:848px;height:157px}
  .role{position:absolute;top:0;height:157px;color:var(--white);font-family:"Oswald",sans-serif;font-weight:500;text-transform:uppercase;font-size:31px;line-height:1.1;white-space:nowrap;overflow:hidden}
  .role small{display:block;font-family:"Arimo",sans-serif;font-size:16px;text-transform:none;line-height:1.2}
  .role.events{left:0;width:198px;background:var(--teal-light);padding:30px 14px;letter-spacing:-0.5px}
  .role.drivers{left:211px;width:211px;background:var(--coral);padding:22px 12px;text-align:center}
  .role.drivers small{text-align:left;margin-top:24px}
  .role.walkers{left:435px;width:199px;background:var(--mustard);padding:24px 10px;text-align:center}
  .role.walkers small{margin-top:24px}
  .role.phone{left:650px;width:198px;background:var(--teal);padding:24px 16px;text-align:center}
  .role.phone small{text-align:left;margin-top:8px}
  .role-shadow{position:absolute;left:0;top:928px;width:848px;height:16px;background:linear-gradient(180deg,#c7c8cb,#e8e9eb)}

  .perks{position:absolute;left:0;top:962px;width:848px;text-align:center;font-family:"Oswald",sans-serif;font-weight:600;font-size:54px;color:var(--coral);line-height:1;white-space:nowrap;letter-spacing:-0.5px}
  .perks .gap{display:inline-block;width:40px}
  .growth{position:absolute;left:0;top:1030px;width:848px;text-align:center;font-family:"Oswald",sans-serif;font-weight:500;font-size:38px;color:var(--dark);line-height:1.15;white-space:nowrap}

  .footer{position:absolute;left:0;top:1120px;width:848px;height:80px;font-family:"Arimo",sans-serif;color:var(--white)}
  .footer svg{position:absolute;inset:0}
  .footer .mail{position:absolute;left:20px;top:8px;font-size:16px;line-height:1.2}
  .footer .office{position:absolute;left:230px;top:8px;width:390px;text-align:center;font-size:16px;line-height:1.2}
  .footer .office b{font-weight:700}
  .footer .phone{position:absolute;left:680px;top:14px;font-size:17px;font-weight:700;line-height:1.45}
</style>
</head>
<body>
<main class="flyer">
  <div class="headline-top">WE'RE</div>
  <div class="headline-main">HIRING</div>

  <div class="candidate">
    <span class="mark"></span>
    <span class="name">Dana Marlowe</span>
    <span class="office">MAYOR</span>
  </div>

  <div class="rule top"></div>
  <div class="photo"></div>
  <div class="photo-people" role="img" aria-label="Photo of six smiling job candidates seated in a row, holding up position signs"></div>
  <h2 class="section-title">POSITIONS INCLUDE</h2>

  <div class="sign office-manager">Office<br>Manager</div>
  <div class="sign office-assistant">Office<br>Assistant</div>
  <div class="sign data-entry">Data Entry<br>Techs</div>
  <div class="sign outreach-manager">Outreach<br>Manager</div>
  <div class="sign asst-outreach">Asst.<br>Outreach<br>Manager</div>
  <div class="rule bottom"></div>

  <section class="roles">
    <div class="role events">Events<br>Coordinator</div>
    <div class="role drivers">Drivers<small>(Must have Personal Car,<br>Insurance &amp;<br>Driver’s License)</small></div>
    <div class="role walkers">Outreach<br>Specialist<small>Walkers</small></div>
    <div class="role phone">Outreach<br>Specialist<small>Phone/Telemarketing<br>(Evenings Only)</small></div>
  </section>
  <div class="role-shadow"></div>

  <p class="perks">EXCELLENT PAY!<span class="gap"></span>FUN ATMOSPHERE !</p>
  <p class="growth">PROMOTIONAL &amp; CAREER ADVANCEMENT<br>OPPORTUNITIES</p>

  <footer class="footer">
    <svg width="848" height="80" viewBox="0 0 848 80" aria-hidden="true">
      <polygon points="0,0 186,0 228,80 0,80" fill="var(--dark)"/>
      <polygon points="204,0 646,0 606,80 246,80" fill="var(--teal)"/>
      <polygon points="664,0 848,0 848,80 624,80" fill="var(--dark)"/>
    </svg>
    <div class="mail">PO Box 4821<br>Fairview,<br>CA 92000</div>
    <div class="office">1280 Harbor Point Avenue, 2nd Floor Atrium<br>Lakeside, CA 92500<br><b>www.marloweformayor.com</b></div>
    <div class="phone">Direct Cell Phone<br>1-555-014-2280</div>
  </footer>
</main>
</body>
</html>
```